Investment Real Estate Firm Needs Template to Showcase properties

We're a firm that sells $1M-$20M Dollar properties. We need a very professional template to be able to insert our information, pictures, and data into it. The data is mostly send via email in PDF and/or printed out. Here's the templates we need using OUR Logo and colors. Name of Company: Harlow Capital Partners

1.)Cover Page Template: I've attached a example but we would like our own original cover page that looks cool and has spot for property photo
2.)Table of Contents Template: I've attached some cool original ideas that we like. Obviously would love our own
3.)Beginning of Section Template: Basically a page letting you know what section you're about ready to start.
4.) Content/Data Template: This is the template where all data will be inserted. So basically just bordering and very minimal space taken up to allow for content to be added
5.) Back Page/Last Page Template: This will be the last page of the presentation or showcase. I can also use this page to insert disclaimers and confidentiality language.

Target Market(s)

This only goes to a targeted personal client base

Industry/Entity Type

Real Estate

Font styles to use
Serif

Requirements
Must have
• - Cover Page, Contents Page, Section Page, Content Page, Back Page
• - Use our Logo. Attached
• - Use Our color scheme
• - Professional Look but some original ideas ;)
• - Abbility for me to edit and Drop in content
Nice to have
• Some Creativity in bordering and maybe carry over the section identity somehow within the border.
• A Extremely light but noticeable transparent "HCP" Logo Only on content pages in background centered " See attached

```html
<!DOCTYPE html>
<html lang="en">
<head>
<meta charset="utf-8">
<title>Harlow Capital Partners – Presentation Template Set</title>
<link href="https://fonts.googleapis.com/css2?family=Raleway:wght@400;500;700;800&display=swap" rel="stylesheet">
<style>
  :root{
    --canvas:#ffffff;
    --grey-light:#b9b9b9;
    --grey-mid:#9a9a9a;
    --grey-dark:#727272;
    --grey-text:#6a6a6a;
    --tan:#c9ab83;
    --white:#ffffff;
    --photo-light:#cfcfcf;
    --photo-dark:#555555;
  }
  html,body{margin:0;padding:0;overflow:hidden;background:var(--canvas);}
  .sheet{position:relative;width:1200px;height:1054px;overflow:hidden;background:var(--canvas);
    font-family:'Raleway',sans-serif;}
  .slide{position:absolute;width:588px;height:331px;display:block;
    box-shadow:0 1px 4px rgba(0,0,0,.25);}
  .slide--cover{left:6px;top:20px}
  .slide--contents{left:606px;top:20px}
  .slide--section-left{left:6px;top:361px}
  .slide--section-right{left:606px;top:361px}
  .slide--content{left:6px;top:697px}
  .slide--back{left:606px;top:697px}
  text{font-family:'Raleway',sans-serif}
  .brand-mark{font-weight:800;fill:var(--grey-text);letter-spacing:-1px}
  .white{fill:var(--white)}
  .b{font-weight:800}
</style>
</head>
<body>
<main class="sheet">

  <svg class="slide slide--cover" viewBox="0 0 628 353" aria-label="Cover page">
    <defs>
      <linearGradient id="bgGrey" x1="0" y1="0" x2="0" y2="1">
        <stop offset="0" stop-color="#bdbdbd"/><stop offset="1" stop-color="#8a8a8a"/>
      </linearGradient>
      <linearGradient id="photoTone" x1="0" y1="0" x2="1" y2="1">
        <stop offset="0" stop-color="#6a6a6a"/><stop offset=".5" stop-color="#c4c4c4"/><stop offset="1" stop-color="#7c7c7c"/>
      </linearGradient>
    </defs>
    <rect width="628" height="353" fill="url(#bgGrey)"/>
    <rect y="334" width="628" height="19" fill="#7d7d7d"/>
    <path role="img" aria-label="Property photo: modern glass and steel building entrance" d="M375,0 C340,120 290,250 235,353 L628,353 L628,0 Z" fill="url(#photoTone)"/>
    <path d="M375,0 C340,120 290,250 235,353" fill="none" stroke="var(--tan)" stroke-width="4"/>
    <path d="M516,0 L604,0 L604,78 Q604,95 588,97 Q560,103 560,118 Q560,103 532,97 Q516,95 516,78 Z" fill="var(--white)" stroke="var(--tan)" stroke-width="2"/>
    <text class="brand-mark" x="560" y="58" font-size="28" text-anchor="middle">HCP</text>
    <text class="white" x="14" y="208" font-size="30">Your Title <tspan class="b">Goes Here</tspan></text>
    <text class="white" x="19" y="225" font-size="11">Your Subtitle Goes Here</text>
    <text x="8" y="346" font-size="6" fill="#a8a8a8">© 2016 HCP. All rights reserved.</text>
  </svg>

  <svg class="slide slide--contents" viewBox="0 0 628 353" aria-label="Table of contents">
    <rect width="628" height="353" fill="url(#bgGrey)"/>
    <path d="M628,85 C600,170 575,260 545,353 L628,353 Z" fill="var(--tan)"/>
    <path d="M527,0 L607,0 L607,74 Q607,88 592,90 Q567,94 567,100 Q567,94 542,90 Q527,88 527,74 Z" fill="var(--white)" stroke="var(--grey-dark)" stroke-width="2"/>
    <text class="brand-mark" x="567" y="58" font-size="26" text-anchor="middle">HCP</text>
    <text class="white" x="75" y="65" font-size="25"><tspan class="b">Table of</tspan> Contents</text>
    <g class="toc" fill="var(--white)" font-size="10">
      <g><text x="75" y="114" font-size="6">01</text><text x="98" y="115">Our Vision &amp; Mission</text><line x1="200" y1="115" x2="252" y2="115" stroke="#eee" stroke-dasharray="1 1"/><text x="256" y="116" font-size="7">Page 07</text></g>
      <g><text x="75" y="138" font-size="6">02</text><text x="98" y="139">About Us</text><line x1="146" y1="139" x2="226" y2="139" stroke="#eee" stroke-dasharray="1 1"/><text x="229" y="140" font-size="7">Page 08</text></g>
      <g><text x="75" y="161" font-size="6">03</text><text x="98" y="162">Our Expertise</text><line x1="166" y1="162" x2="238" y2="162" stroke="#eee" stroke-dasharray="1 1"/><text x="241" y="163" font-size="7">Page 10</text></g>
      <g><text x="75" y="184" font-size="6">04</text><text x="98" y="185">Beautiful Fully Furnished Unit in Lenox</text><line x1="287" y1="185" x2="309" y2="185" stroke="#eee" stroke-dasharray="1 1"/><text x="312" y="186" font-size="7">Page 11</text></g>
      <g><text x="75" y="207" font-size="6">05</text><text x="98" y="208">Gorgeous Condo in Downtown Pittsfield</text><line x1="292" y1="208" x2="314" y2="208" stroke="#eee" stroke-dasharray="1 1"/><text x="317" y="209" font-size="7">Page 14</text></g>
      <g><text x="75" y="229" font-size="6">06</text><text x="98" y="230">Portfolio Area</text><line x1="168" y1="230" x2="261" y2="230" stroke="#eee" stroke-dasharray="1 1"/><text x="264" y="231" font-size="7">Page 15</text></g>
      <g><text x="75" y="253" font-size="6">07</text><text x="98" y="254">Our Services</text><line x1="163" y1="254" x2="237" y2="254" stroke="#eee" stroke-dasharray="1 1"/><text x="240" y="255" font-size="7">Page 17</text></g>
      <g><text x="75" y="277" font-size="6">08</text><text x="98" y="278">Text Area</text><line x1="148" y1="278" x2="226" y2="278" stroke="#eee" stroke-dasharray="1 1"/><text x="229" y="279" font-size="7">Page 18</text></g>
    </g>
  </svg>

  <svg class="slide slide--section-left" viewBox="0 0 628 353" aria-label="Section opener with photo on the right">
    <defs>
      <linearGradient id="bridgeTone" x1="0" y1="0" x2="1" y2="1">
        <stop offset="0" stop-color="#9a9a9a"/><stop offset=".6" stop-color="#d0d0d0"/><stop offset="1" stop-color="#5e5e5e"/>
      </linearGradient>
    </defs>
    <rect role="img" aria-label="Property photo: glass walkway with steel beams" width="628" height="353" fill="url(#bridgeTone)"/>
    <path d="M0,0 L460,0 C420,120 370,250 330,353 L0,353 Z" fill="#c9c6c2" opacity=".92"/>
    <circle cx="85" cy="213" r="20" fill="none" stroke="var(--white)" stroke-width="5"/>
    <text class="white" x="46" y="270" font-size="30"><tspan class="b">Section</tspan> Break</text>
    <g class="white" font-size="10">
      <text x="49" y="285">Lorem Ipsum dolor sit amer, consectetur</text>
      <text x="49" y="297">adipiscing elit, sed do eiusmod tempor</text>
      <text x="49" y="310">incididunt ut labore et commodo consequat</text>
      <text x="49" y="322">dolore magna aliqua.</text>
    </g>
    <path d="M628,250 L560,250 Q533,250 533,280 L533,310 Q533,338 560,338 L628,338" fill="var(--white)" stroke="var(--tan)" stroke-width="2"/>
    <text class="brand-mark" x="580" y="304" font-size="26" text-anchor="middle">HCP</text>
  </svg>

  <svg class="slide slide--section-right" viewBox="0 0 628 353" aria-label="Section opener with photo on the left">
    <defs>
      <linearGradient id="cityTone" x1="0" y1="0" x2="0" y2="1">
        <stop offset="0" stop-color="#8a8a8a"/><stop offset=".5" stop-color="#4a4a4a"/><stop offset="1" stop-color="#6a6a6a"/>
      </linearGradient>
    </defs>
    <rect role="img" aria-label="Photo: downtown city skyline with highway" width="628" height="353" fill="url(#cityTone)"/>
    <path d="M455,0 C400,110 340,230 295,353 L628,353 L628,0 Z" fill="url(#bgGrey)"/>
    <path d="M455,0 C400,110 340,230 295,353" fill="none" stroke="var(--tan)" stroke-width="4"/>
    <path d="M17,5 L105,5 L105,78 Q105,95 88,97 Q61,100 45,98 Q17,95 17,78 Z" fill="var(--white)" stroke="var(--grey-dark)" stroke-width="2"/>
    <text class="brand-mark" x="61" y="62" font-size="28" text-anchor="middle">HCP</text>
    <circle cx="536" cy="215" r="20" fill="none" stroke="var(--white)" stroke-width="5"/>
    <text class="white" x="578" y="268" font-size="30" text-anchor="end">Section <tspan class="b">Break</tspan></text>
    <g class="white" font-size="10" text-anchor="end">
      <text x="577" y="283">Lorem Ipsum dolor sit amer, consectetur</text>
      <text x="577" y="296">adipiscing elit, sed do eiusmod tempor</text>
      <text x="577" y="309">incididunt ut labore et commodo consequat</text>
      <text x="577" y="321">dolore magna aliqua.</text>
    </g>
  </svg>

  <svg class="slide slide--content" viewBox="0 0 628 353" aria-label="Content page">
    <rect width="628" height="353" fill="var(--white)"/>
    <text x="27" y="51" font-size="28" fill="var(--grey-text)"><tspan class="b">Your Title</tspan> Goes Here</text>
    <rect x="32" y="60" width="42" height="2.5" fill="var(--tan)"/>
    <text class="brand-mark" x="567" y="58" font-size="34" text-anchor="middle">HCP</text>
    <rect x="0" y="334" width="583" height="19" fill="var(--grey-dark)"/>
    <rect x="605" y="334" width="23" height="19" fill="var(--tan)"/>
    <text x="594" y="347" font-size="8" fill="#999" text-anchor="middle">5</text>
    <text x="8" y="346" font-size="6" fill="#dcdcdc">© 2016 HCP. All rights reserved.</text>
  </svg>

  <svg class="slide slide--back" viewBox="0 0 628 353" aria-label="Back page with contact details">
    <defs>
      <linearGradient id="iconGrey" x1="0" y1="0" x2="0" y2="1">
        <stop offset="0" stop-color="#a5a5a5"/><stop offset="1" stop-color="#6b6b6b"/>
      </linearGradient>
    </defs>
    <rect width="628" height="353" fill="var(--white)"/>
    <text class="brand-mark" x="314" y="130" font-size="78" text-anchor="middle">HCP</text>
    <g class="contact">
      <circle cx="130" cy="191" r="12" fill="url(#iconGrey)"/>
      <path d="M124,192 L130,186 L136,192 L134,192 L134,197 L126,197 L126,192 Z" fill="var(--white)"/>
      <circle cx="253" cy="191" r="12" fill="url(#iconGrey)"/>
      <path d="M249,186 Q248,192 253,196 L257,197 L258,194 L255,193 L254,194 Q251,192 251,190 L252,189 L251,186 Z" fill="var(--white)"/>
      <circle cx="377" cy="191" r="12" fill="url(#iconGrey)"/>
      <rect x="371" y="187" width="12" height="8" fill="var(--white)"/>
      <path d="M371,187 L377,192 L383,187" fill="none" stroke="#888" stroke-width="1"/>
      <circle cx="500" cy="191" r="12" fill="url(#iconGrey)"/>
      <circle cx="500" cy="191" r="5.5" fill="none" stroke="var(--white)" stroke-width="1.5"/>
      <line x1="494.5" y1="191" x2="505.5" y2="191" stroke="var(--white)" stroke-width="1"/>
      <g font-size="10" fill="var(--grey-text)" text-anchor="middle">
        <text x="130" y="221">123 Street Road</text>
        <text x="130" y="234">City 12345</text>
        <text x="253" y="221">(123) 456-7890</text>
        <text x="377" y="221">name@email.com</text>
        <text x="494" y="221">www.website-address.com</text>
      </g>
    </g>
    <path d="M0,268 Q314,345 628,262 L628,353 L0,353 Z" fill="url(#bgGrey)"/>
    <path d="M0,264 Q314,341 628,258" fill="none" stroke="var(--tan)" stroke-width="3"/>
    <g fill="var(--white)">
      <circle cx="288" cy="330" r="7"/>
      <circle cx="314" cy="330" r="7"/>
      <circle cx="340" cy="330" r="7"/>
    </g>
  </svg>

</main>
</body>
</html>
```